Promotion flyer for chair massage

What i need is a design for a 2 page flyer. Im gonna give it to a company so their employe can learn about the service and how they can take an appointements with us. The text is in french because i work in a french company.
On first page(FRONT PAGE) i want the name of the company VELORAMAX inc.
and bellow : Massothérapie sur chaise en entreprise
On the second page(INSIDE) i want the benefits :
Les Bienfaits
- DIMINUTION DU STRESS
- AMÉLIORATION DU BIEN-ÊTRE PHYSIQUE ET PSYCHOLOGIQUE
- AUGMENTATION DE L’ÉNERGIE
- SOULAGE LES MAUX DE DOS ET DE TÊTE
- AMÉLIORE VOTRE QUALITÉ DE SOMMEIL
On the third page (INSIDE) I want the steps to take an appointment :
Obtenez votre massage en quelques clics
1. Allez sur https://www.bookalyte.example/veloramax
2. Choisir le nombre de minute désirer (10-15-20-30)
3. Choisir votre thérapeute
4. Choisir votre emplacement (lieu de travail)
5. Choisir votre plage horaire
6. Remplir votre fiche (Prénom-Nom-Email-#téléphone)
7. Aussi simple que ça !! À bientôt !
On the final page i want the text so they can contact me :
CONTACTEZ-NOUS
Mail : Info@veloramax.example
Tél. 514-276-9032
Site web : Veloramax.example
If you can respect the same kind of design that i already did in the past i would love it :)
Bank employee
Massage Therapy

```html
<!DOCTYPE html>
<html lang="fr">
<head>
<meta charset="utf-8">
<title>VELORAMAX — Dépliant massothérapie sur chaise</title>
<link href="https://fonts.googleapis.com/css2?family=Open+Sans:ital,wght@0,400;0,600;0,700;0,800;1,400;1,700&display=swap" rel="stylesheet">
<style>
:root{
  --bg:#585858;
  --blue:#2f5fc4;
  --blue-deep:#2450b0;
  --cyan:#4cc3db;
  --cyan-light:#8bdcea;
  --icon:#2a9fd8;
  --ink:#2b2b2b;
  --muted:#8a8a8a;
  --cream:#f8f6ea;
  --paper:#f1f1ee;
}
*{margin:0;padding:0;box-sizing:border-box}
html,body{width:1200px;height:1200px;overflow:hidden;background:var(--bg)}
body{font-family:"Open Sans",sans-serif;color:var(--ink);position:relative}
ul,ol{list-style:none}
.spread{position:absolute;left:60px;width:1080px;height:540px;display:flex;box-shadow:0 16px 40px rgba(0,0,0,.35)}
.spread-outside{top:36px}
.spread-inside{top:624px}
.page{position:relative;width:540px;height:540px;overflow:hidden;background:linear-gradient(160deg,var(--paper) 0%,var(--cream) 45%,var(--cream) 100%)}
.page svg.band{position:absolute;left:0;width:540px}
.band-top{top:0}
.band-bottom{bottom:0}
.section-head{position:absolute;display:flex;align-items:center;gap:14px}
.section-head h2{font-weight:700;font-size:19px;letter-spacing:1px;text-transform:uppercase;line-height:1.15}
.section-head p{font-size:9px;font-weight:600;letter-spacing:.5px;text-transform:uppercase;margin-top:3px}
.section-head .rule{width:26px;height:2px;background:var(--ink);margin-top:7px}

/* Back page: contact */
.contact{position:absolute;left:60px;top:150px;width:420px}
.contact h2{font-size:26px;font-weight:800;letter-spacing:1px;text-transform:uppercase}
.contact .rule{width:30px;height:2px;background:var(--ink);margin:10px 0 30px}
.contact-list{display:flex;flex-direction:column;gap:20px}
.contact-item{display:flex;align-items:center;gap:16px;font-size:15px}
.contact-item b{font-weight:700;margin-right:4px}

/* Front cover */
.cover-photo{position:absolute;left:0;top:0;width:540px;height:330px;background:linear-gradient(160deg,#6d7fb8 0%,#7a4d5c 45%,#3c2f3a 75%,#24262e 100%)}
.brand{position:absolute;left:50px;top:380px;display:flex;align-items:center;gap:14px}
.brand-name{font-size:40px;font-weight:800;letter-spacing:.5px;text-transform:uppercase;line-height:1}
.brand-dot{width:30px;height:30px;border-radius:50%;background:var(--icon);flex:none}
.brand-tagline{position:absolute;left:52px;top:432px;font-size:12px;font-weight:600;letter-spacing:1.2px;text-transform:uppercase}

/* Benefits */
.benefits{position:absolute;left:36px;top:108px;width:468px;display:grid;grid-template-columns:repeat(3,minmax(0,1fr));row-gap:16px;column-gap:10px}
.benefit{display:flex;align-items:center;gap:8px}
.benefit svg{flex:none}
.benefit span{font-size:8.5px;font-weight:700;text-transform:uppercase;line-height:1.3;letter-spacing:.3px}

/* Photo grid */
.photo-grid{position:absolute;left:40px;top:222px;width:460px;display:grid;grid-template-columns:repeat(3,minmax(0,1fr));grid-template-rows:118px 118px;gap:8px}
.photo{border:4px solid #fff;box-shadow:0 2px 6px rgba(0,0,0,.15)}
.photo.a{background:linear-gradient(150deg,#e6e8ea,#9ea4ad 60%,#3b3f48)}
.photo.b{background:linear-gradient(150deg,#dfe2e6,#8b929c 55%,#2e323a)}
.photo.c{background:linear-gradient(150deg,#c9b7a6,#6c6360 55%,#2c2b2e)}
.photo.d{background:linear-gradient(150deg,#e2e4e8,#a2a7ae 55%,#4a4f57)}
.photo.e{background:linear-gradient(150deg,#b69277,#6a5a50 55%,#2f2a28)}
.photo.f{background:linear-gradient(150deg,#d6d8dc,#c7a989 55%,#4e4540)}

/* Steps */
.steps{position:absolute;left:22px;top:136px;width:496px;display:grid;grid-template-columns:repeat(6,minmax(0,1fr));gap:5px}
.step{display:flex;flex-direction:column;align-items:center;gap:6px;min-width:0}
.step .card{width:100%;height:58px;background:#fff;box-shadow:0 3px 6px rgba(0,0,0,.18);clip-path:polygon(0 0,88% 0,100% 50%,88% 100%,0 100%);padding:5px 10px 5px 5px;font-size:7px;line-height:1.3;text-align:center;display:flex;align-items:center;justify-content:center;overflow-wrap:anywhere}
.step-final{position:absolute;left:0;width:540px;top:236px;text-align:center;font-size:10px;font-weight:700;letter-spacing:.5px;color:var(--icon)}

/* Testimonials */
.testimonial-photo{position:absolute;left:0;top:262px;width:540px;height:98px;background:linear-gradient(100deg,#3a3d44 0%,#6a6e78 40%,#8d7478 70%,#3f3a3e 100%)}
.testimonial-label{position:absolute;left:196px;top:290px;display:flex;align-items:center;gap:12px;color:#fff}
.testimonial-label h2{font-size:17px;font-weight:700;letter-spacing:1px;text-transform:uppercase}
.testimonial-label .rule{width:26px;height:2px;background:#fff;margin-top:5px}
.testimonials{position:absolute;left:26px;top:374px;width:488px;display:grid;grid-template-columns:repeat(3,minmax(0,1fr));gap:18px}
.quote{font-size:8.5px;line-height:1.4}
.quote cite{display:block;text-align:right;margin-top:6px;font-style:italic;font-weight:700;font-size:9px;color:var(--muted)}
.quote cite small{display:block;font-weight:400;font-style:normal;font-size:7.5px}
</style>
</head>
<body>

<!-- Outside spread: back page and front cover -->
<main class="spread spread-outside">

  <section class="page page-back">
    <svg class="band band-top" height="80" viewBox="0 0 540 80" aria-hidden="true">
      <polygon points="0,0 540,0 540,40 320,20 120,50 0,25" fill="var(--cyan)"/>
      <polygon points="0,0 240,0 110,32 0,14" fill="var(--cyan-light)" opacity=".7"/>
    </svg>

    <div class="contact">
      <h2>Contactez-nous</h2>
      <div class="rule"></div>
      <ul class="contact-list">
        <li class="contact-item">
          <svg width="30" height="30" viewBox="0 0 30 30" fill="none" stroke="var(--icon)" stroke-width="2"><rect x="3" y="7" width="24" height="16" rx="2"/><path d="M3 8l12 9 12-9"/></svg>
          <span><b>Mail :</b>Info@veloramax.example</span>
        </li>
        <li class="contact-item">
          <svg width="30" height="30" viewBox="0 0 30 30" fill="none" stroke="var(--icon)" stroke-width="2"><path d="M8 3h5l2 6-3 2c1 3 4 6 7 7l2-3 6 2v5c0 2-2 3-4 3C12 25 5 18 5 7c0-2 1-4 3-4z"/></svg>
          <span><b>Tél.</b>514-276-9032</span>
        </li>
        <li class="contact-item">
          <svg width="30" height="30" viewBox="0 0 30 30" fill="none" stroke="var(--icon)" stroke-width="2"><circle cx="15" cy="15" r="11"/><path d="M4 15h22M15 4c4 4 4 18 0 22M15 4c-4 4-4 18 0 22"/></svg>
          <span><b>Site web :</b>Veloramax.example</span>
        </li>
      </ul>
    </div>

    <svg class="band band-bottom" height="80" viewBox="0 0 540 80" aria-hidden="true">
      <polygon points="0,20 200,50 380,25 540,45 540,80 0,80" fill="var(--blue)"/>
      <polygon points="0,50 260,70 540,66 540,80 0,80" fill="var(--blue-deep)"/>
    </svg>
  </section>

  <section class="page page-cover">
    <div class="cover-photo" role="img" aria-label="Thérapeute massant le bas du dos d'un employé assis"></div>
    <svg class="band" style="top:250px" height="130" viewBox="0 0 540 130" aria-hidden="true">
      <polygon points="0,40 260,80 540,20 540,130 0,130" fill="var(--paper)"/>
      <polygon points="0,40 260,80 0,130" fill="#ffffff" opacity=".6"/>
    </svg>
    <div class="brand">
      <span class="brand-name">VELORAMAX inc.</span>
      <span class="brand-dot" aria-hidden="true"></span>
    </div>
    <p class="brand-tagline">Massothérapie sur chaise en entreprise</p>
    <svg class="band band-bottom" height="40" viewBox="0 0 540 40" aria-hidden="true">
      <polygon points="0,30 300,18 540,0 540,40 0,40" fill="var(--blue)"/>
    </svg>
  </section>

</main>

<!-- Inside spread: benefits and booking -->
<main class="spread spread-inside">

  <section class="page page-benefits">
    <svg class="band band-top" height="110" viewBox="0 0 540 110" aria-hidden="true">
      <polygon points="420,0 540,0 540,110" fill="var(--blue)"/>
      <polygon points="455,0 540,0 540,60" fill="var(--blue-deep)"/>
    </svg>

    <header class="section-head" style="left:40px;top:36px">
      <svg width="38" height="46" viewBox="0 0 44 52" fill="none" stroke="var(--ink)" stroke-width="2">
        <path d="M4 2h26l10 10v38H4z"/><path d="M30 2v10h10"/>
        <path d="M12 22l4 4 4-4M12 30l4 4 4-4M22 22l4 4 4-4M22 30l4 4 4-4"/>
      </svg>
      <div>
        <h2>Les bienfaits</h2>
        <p>D'un programme de massage sur chaise</p>
        <div class="rule"></div>
      </div>
    </header>

    <ul class="benefits">
      <li class="benefit">
        <svg width="30" height="30" viewBox="0 0 34 34" fill="none" stroke="var(--icon)" stroke-width="2"><path d="M3 26c6-4 10-4 16-2h6"/><path d="M17 20c0-8 4-12 10-14-1 8-4 12-10 14z"/><path d="M17 20c-1-6-4-9-9-10 0 6 3 9 9 10z"/></svg>
        <span>Diminution<br>du stress</span>
      </li>
      <li class="benefit">
        <svg width="30" height="30" viewBox="0 0 34 34" fill="none" stroke="var(--icon)" stroke-width="2"><circle cx="17" cy="14" r="7"/><path d="M13 24h8M14 28h6M17 3V1M7 6 5 4M27 6l2-2M4 14H2M30 14h2"/></svg>
        <span>Amélioration du bien-être physique et psychologique</span>
      </li>
      <li class="benefit">
        <svg width="30" height="30" viewBox="0 0 34 34" fill="none" stroke="var(--icon)" stroke-width="2"><path d="M17 4c5 7 7 10 7 14a7 7 0 0 1-14 0c0-4 2-7 7-14z"/><path d="M4 26c8 6 18 6 26 0"/></svg>
        <span>Augmentation<br>de l'énergie</span>
      </li>
      <li class="benefit">
        <svg width="30" height="30" viewBox="0 0 34 34" fill="none" stroke="var(--icon)" stroke-width="2"><circle cx="13" cy="10" r="6"/><path d="M3 31c0-8 4-12 10-12s10 4 10 12"/><path d="M22 8a5 5 0 0 1 0 10M26 20c3 2 5 6 5 11"/></svg>
        <span>Soulage les maux<br>de dos et de tête</span>
      </li>
      <li class="benefit">
        <svg width="30" height="30" viewBox="0 0 34 34" fill="none" stroke="var(--icon)" stroke-width="2"><circle cx="19" cy="15" r="11"/><path d="M19 9v6l4 3"/><path d="M2 30h14M4 26l3 4"/></svg>
        <span>Améliore votre<br>qualité de sommeil</span>
      </li>
    </ul>

    <div class="photo-grid">
      <div class="photo a" role="img" aria-label="Thérapeute massant un employé assis sur une chaise de massage"></div>
      <div class="photo b" role="img" aria-label="Séance de massage sur chaise dans un bureau"></div>
      <div class="photo c" role="img" aria-label="Employée recevant un massage des épaules"></div>
      <div class="photo d" role="img" aria-label="Thérapeute ajustant la chaise de massage"></div>
      <div class="photo e" role="img" aria-label="Massage du dos sur chaise près des fenêtres"></div>
      <div class="photo f" role="img" aria-label="Massage de la nuque d'une employée"></div>
    </div>

    <svg class="band band-bottom" height="70" viewBox="0 0 540 70" aria-hidden="true">
      <polygon points="0,10 170,36 350,16 540,42 540,70 0,70" fill="var(--cyan)"/>
      <polygon points="0,36 140,54 300,42 540,62 540,70 0,70" fill="var(--cyan-light)" opacity=".7"/>
      <polygon points="350,16 540,42 540,22" fill="var(--blue)" opacity=".5"/>
    </svg>
  </section>

  <section class="page page-booking">
    <svg class="band band-top" height="60" viewBox="0 0 540 60" aria-hidden="true">
      <polygon points="0,0 540,0 540,48 320,28 120,42 0,20" fill="var(--cyan)"/>
      <polygon points="0,0 250,0 120,28 0,14" fill="var(--cyan-light)" opacity=".7"/>
    </svg>

    <header class="section-head" style="left:56px;top:64px">
      <svg width="50" height="36" viewBox="0 0 56 40" fill="none" stroke="var(--ink)" stroke-width="2.4"><rect x="8" y="3" width="40" height="27" rx="2"/><path d="M2 34h52l-3 4H5z"/></svg>
      <div>
        <h2>Obtenez votre massage<br>en quelques clics</h2>
        <div class="rule"></div>
      </div>
    </header>

    <ol class="steps">
      <li class="step">
        <svg width="22" height="20" viewBox="0 0 24 22" fill="none" stroke="var(--icon)" stroke-width="1.8"><rect x="4" y="2" width="16" height="12" rx="1"/><path d="M1 17h22l-2 3H3z"/></svg>
        <div class="card">Allez sur www.bookalyte.example/ veloramax</div>
      </li>
      <li class="step">
        <svg width="22" height="20" viewBox="0 0 24 22" fill="none" stroke="var(--icon)" stroke-width="1.8"><circle cx="12" cy="12" r="9"/><path d="M12 12l4-4M7 12h1M16 12h1M12 6v1"/></svg>
        <div class="card">Sélectionnez votre durée (10-15-20-30)</div>
      </li>
      <li class="step">
        <svg width="22" height="20" viewBox="0 0 24 22" fill="none" stroke="var(--icon)" stroke-width="1.8"><circle cx="12" cy="7" r="5"/><path d="M3 21c0-5 4-8 9-8s9 3 9 8z"/></svg>
        <div class="card">Choisir votre thérapeute</div>
      </li>
      <li class="step">
        <svg width="22" height="20" viewBox="0 0 24 22" fill="none" stroke="var(--icon)" stroke-width="1.8"><path d="M2 4l6-2 8 3 6-2v15l-6 2-8-3-6 2z"/><circle cx="16" cy="10" r="2.5"/></svg>
        <div class="card">Choisir votre emplacement (lieu de travail)</div>
      </li>
      <li class="step">
        <svg width="22" height="20" viewBox="0 0 24 22" fill="none" stroke="var(--icon)" stroke-width="1.8"><circle cx="12" cy="11" r="9"/><path d="M12 5v6l3 3"/></svg>
        <div class="card">Choisir votre plage horaire</div>
      </li>
      <li class="step">
        <svg width="22" height="20" viewBox="0 0 24 22" fill="none" stroke="var(--icon)" stroke-width="1.8"><path d="M5 1h10l5 5v15H5z"/><path d="M9 11h7M9 15h7"/></svg>
        <div class="card">Remplir votre fiche (Nom, email et téléphone)</div>
      </li>
    </ol>
    <p class="step-final">Aussi simple que ça !! À bientôt !</p>

    <div class="testimonial-photo" role="img" aria-label="Employés souriants assis dans un bureau après leur massage"></div>
    <div class="testimonial-label">
      <svg width="42" height="36" viewBox="0 0 46 40" fill="none" stroke="#fff" stroke-width="2.2"><rect x="18" y="2" width="26" height="17" rx="2"/><path d="M24 19l-2 5 6-5"/><circle cx="13" cy="18" r="6"/><path d="M2 38c0-7 5-11 11-11s11 4 11 11"/></svg>
      <div>
        <h2>Témoignages</h2>
        <div class="rule"></div>
      </div>
    </div>

    <div class="testimonials">
      <figure class="quote">
        <blockquote>« Je ne crois pas que 15 minutes suffisent à me détendre à ce point. J'attends impatiemment ce petit plaisir hebdomadaire. »</blockquote>
        <cite>Odile<small>Réceptionniste</small></cite>
      </figure>
      <figure class="quote">
        <blockquote>« Je me suis tout de suite sentie en confiance avec Félix. Ce beau moment de relaxation m'a permis de me revigorer pour passer la période des fêtes. »</blockquote>
        <cite>Maëlle<small>Directrice des ventes</small></cite>
      </figure>
      <figure class="quote">
        <blockquote>« Très professionnel, ce massage m'a procuré une détente instantanée. Je me suis senti bien, mes épaules et mon cou se sont relâchés. »</blockquote>
        <cite>Armand<small>Propriétaire</small></cite>
      </figure>
    </div>

    <svg class="band band-bottom" height="46" viewBox="0 0 540 46" aria-hidden="true">
      <polygon points="0,4 200,26 400,12 540,28 540,46 0,46" fill="var(--blue)"/>
      <polygon points="0,26 240,40 540,40 540,46 0,46" fill="var(--blue-deep)"/>
    </svg>
  </section>

</main>
</body>
</html>
```